Real Estate Company Looking for Business Card Designs for 3 Executives

Hello!
Thanks so much for considering our project! We are a real estate investment company located in Edmonton, Alberta called Bellcrane Group of Companies. We invest/develop both commercial and residential real estate and are looking to create 3 DOUBLE-SIDED business cards for 3 top executives in the company! (for some reason it won't let us select the double-sided option, but yes, the cards are double sided and would be happy to tip extra)

We have certain guidelines that we want our business cards to for sure follow - the back of the Business card has to be the Black Background Version of the Logo which has already been designed and linked as a file (first file). We want the entire back of the card to simply just be the black background logo. In terms of the front of the card, would like to see a smaller version of the white background logo (linked as the second file) in the top left hand corner - of course, feel free to get creative and we can make revisions together along the way! and Then after that, just text. We want the card to be sharp, clean, easy on the eyes and highly professional looking. We would like the card to include the Full name of the Company (Bellcrane Group of Companies), Name of the Person, Title, Phone, Email. If possible please provide the front part of the card for 3 people:

1) Bellcrane Group of Companies, Nora Lindqvist, Chief Financial Officer, 780-555-0142, noralindqvist@bellcranegroup.example

2) Bellcrane Group of Companies, Julien Lindqvist, Chief Executive Officer, 780-555-0187, julienlindqvist@bellcranegroup.example

3) Bellcrane Group of Companies, Tom Okafor, Chief Operations Officer, 587-555-0163, tomokafor@bellcranegroup.example

Thank you so much for considering our project & we look forward to seeing your designs!

```html
<!DOCTYPE html>
<html lang="en">
<head>
<meta charset="utf-8">
<title>Bellcrane Business Cards</title>
<link rel="stylesheet" href="https://fonts.googleapis.com/css2?family=Barlow+Condensed:wght@300;400;600;700&display=swap">
<style>
  :root {
    --ink: #050608;
    --paper: #ffffff;
    --backdrop: #f1f1f2;
    --card-w: 308px;
    --card-h: 539px;
  }
  * { margin: 0; padding: 0; box-sizing: border-box; }
  html, body {
    width: 1200px;
    height: 848px;
    overflow: hidden;
  }
  body {
    background: var(--backdrop);
    position: relative;
    font-family: "Barlow Condensed", "Arial Narrow", sans-serif;
  }
  .card {
    position: absolute;
    top: 155px;
    width: var(--card-w);
    height: var(--card-h);
    overflow: hidden;
  }
  .card--front {
    left: 233px;
    background: var(--paper);
    border: 1px solid var(--ink);
  }
  .card--back {
    left: 660px;
    background: var(--ink);
  }

  /* front: wordmark */
  .wordmark {
    position: absolute;
    top: 150px;
    left: 0;
    width: 100%;
    text-align: center;
    font-weight: 400;
    font-size: 24px;
    letter-spacing: 10px;
    padding-left: 10px;
    color: var(--ink);
  }

  /* front: person */
  .person {
    position: absolute;
    top: 262px;
    left: 0;
    width: 100%;
    text-align: center;
    color: var(--ink);
  }
  .person__name {
    display: inline-block;
    font-weight: 700;
    font-size: 27px;
    line-height: 32px;
    padding: 0 4px 2px;
    border-bottom: 1px solid var(--ink);
  }
  .person__title {
    font-weight: 300;
    font-size: 17px;
    margin-top: 2px;
  }

  /* front: stripes and contact band */
  .stripes {
    position: absolute;
    top: 366px;
    left: 0;
    width: 100%;
  }
  .stripes span {
    display: block;
    height: 3px;
    background: var(--ink);
    margin-bottom: 5px;
  }
  .contact-band {
    position: absolute;
    top: 383px;
    left: 0;
    width: 100%;
    bottom: 0;
    background: var(--ink);
    color: var(--paper);
    text-align: center;
  }
  .contact {
    list-style: none;
    margin-top: 23px;
    font-weight: 300;
    font-size: 17px;
    line-height: 26px;
  }
  .contact li {
    display: flex;
    justify-content: center;
    align-items: center;
    gap: 6px;
  }
  .contact__email { font-size: 15.5px; }
  .contact svg { fill: var(--paper); flex: none; }
  .company {
    margin-top: 20px;
    font-weight: 600;
    font-size: 16px;
    letter-spacing: 2px;
    line-height: 23px;
    text-transform: uppercase;
  }

  /* back */
  .back-wordmark {
    position: absolute;
    left: 50%;
    top: 50%;
    transform: translate(-50%, -50%) rotate(-90deg);
    white-space: nowrap;
    color: var(--paper);
    font-weight: 400;
    font-size: 34px;
    letter-spacing: 14px;
    padding-left: 14px;
  }
</style>
</head>
<body>

  <section class="card card--front" aria-label="Business card front">
    <div class="wordmark">BELLCRANE</div>

    <div class="person">
      <div class="person__name">Nora Lindqvist</div>
      <div class="person__title">Chief Financial Officer</div>
    </div>

    <div class="stripes" aria-hidden="true"><span></span><span></span></div>

    <div class="contact-band">
      <ul class="contact">
        <li>
          <svg width="13" height="15" viewBox="0 0 24 24" aria-hidden="true">
            <path d="M6.6 10.8a15.1 15.1 0 0 0 6.6 6.6l2.2-2.2a1 1 0 0 1 1-.25 11.4 11.4 0 0 0 3.6.57 1 1 0 0 1 1 1V20a1 1 0 0 1-1 1A17 17 0 0 1 3 4a1 1 0 0 1 1-1h3.5a1 1 0 0 1 1 1c0 1.25.2 2.45.57 3.6a1 1 0 0 1-.25 1z"/>
          </svg>
          <span>780-555-0142</span>
        </li>
        <li class="contact__email">
          <svg width="16" height="12" viewBox="0 0 24 18" aria-hidden="true">
            <path d="M0 0h24v18H0z M2 2v.4l10 7.2 10-7.2V2z M2 4.8V16h20V4.8l-10 7.2z" fill-rule="evenodd"/>
          </svg>
          <span>noralindqvist@bellcranegroup.example</span>
        </li>
      </ul>
      <p class="company">Bellcrane Group<br>of Companies</p>
    </div>
  </section>

  <section class="card card--back" aria-label="Business card back">
    <div class="back-wordmark">BELLCRANE</div>
  </section>

</body>
</html>
```